Lanterns on the Tide

I need a book cover design for a world history book written for a target audience of high school students and progressive teachers. The book is more balanced towards a world history perspective than a Western-leaning perspective. The first 500 pages deal with the major turning points in world history - from the first hominids that roamed Africa to the end of the Cold War, and the final 100 pages cover the major challenges facing the world today. The book is 95% graphic details, hopefully-engaging stories and needed facts, but there is a bit of sarcasm, verbal irony and asides thrown in to keep the reader's eyes from glossing over. I would need a cover that would appeal to any school teacher, but something that would not scare off students or the average Joe off the street.
Updates

One added note, please leave the bottom right corner -  2" height by 3" width free of text/image for the ISBN code.

As far as a central image goes, it needs to be a dynamic (avoid something readers would readily see elsewhere in their lives) image, or nothing at all.  Also, please justify all text on the back cover to the left side (avoid centering).

Reason: A few people have voiced an interest in having the deadline extended through next weekend to allow for some alterations and also the ability to take advantage of the upcoming holidays. I will take you up on this request. Thank you all again for your submissions. i've seen some very unique takes on the story/tone of the book.

Industry/Entity Type

High School

Requirements
Must have
• I've enclosed a PDF with the text for the front and back cover.

On the back cover, I'd like the quote and the initial question to stand out. I'd like the initial question to be in lower case.

For the spine, I'd like the title font to match the title front from the front cover.

The book cover needs to measure 9.25" by 13.75" with a 1.5" spine. Allow .125 inches for the bleed.

I've attached a Word Document with all the text. The layout is just a suggestion.
Should not have
• I do not want any stock images that I'll need to pay for.

```html
<!DOCTYPE html>
<html lang="en">
<head>
<meta charset="utf-8">
<title>Lanterns on the Tide — Book Cover</title>
<link href="https://fonts.googleapis.com/css2?family=Bodoni+Moda:opsz,wght@6..96,900&family=Tinos:ital,wght@0,400;0,700;1,400;1,700&family=Stardos+Stencil:wght@700&family=Arimo:wght@400;700&display=swap" rel="stylesheet">
<style>
  :root {
    --cover-red: #ff0000;
    --headline-gold: #ffb62b;
    --quote-gold: #ffcc1a;
    --ink: #000000;
    --paper: #ffffff;
    --muted: #a6a6a6;
  }
  * { margin: 0; padding: 0; box-sizing: border-box; }
  html, body {
    width: 1200px;
    height: 825px;
    overflow: hidden;
    background: var(--cover-red);
  }
  .cover {
    position: relative;
    width: 1200px;
    height: 825px;
    background: var(--cover-red);
    color: var(--ink);
    font-family: "Tinos", "Times New Roman", serif;
  }

  /* Back panel */
  .back {
    position: absolute;
    left: 0; top: 0;
    width: 556px; height: 825px;
  }
  .back-question {
    position: absolute;
    left: 14px; top: 12px;
    width: 542px;
    font-family: "Tinos", "Times New Roman", serif;
    font-weight: 700;
    font-size: 45px;
    line-height: 55px;
    color: var(--headline-gold);
    white-space: nowrap;
  }
  .blurb {
    position: absolute;
    left: 11px;
    font-size: 16px;
    line-height: 20px;
    letter-spacing: 0.2px;
    text-align: left;
    white-space: nowrap;
  }
  .blurb em { font-style: italic; }
  .blurb-1 { top: 171px; }
  .blurb-2 { top: 318px; }
  .blurb-3 { top: 480px; }
  .endorsement {
    position: absolute;
    left: 9px; top: 605px;
    font-size: 18px;
    line-height: 24px;
    letter-spacing: -0.1px;
    font-style: italic;
    color: var(--quote-gold);
    white-space: nowrap;
  }
  .endorsement cite {
    font-style: normal;
    font-weight: 700;
    color: var(--ink);
  }
  .isbn-block {
    position: absolute;
    left: 359px; top: 692px;
    width: 180px; height: 119px;
    background: var(--paper);
  }
  .publisher-band {
    position: absolute;
    left: 1px; top: 10px;
    width: 178px; height: 31px;
    background: var(--ink);
    color: var(--paper);
    font-size: 15px;
    line-height: 31px;
    padding-left: 6px;
    white-space: nowrap;
  }
  .isbn-number {
    position: absolute;
    left: 11px; top: 48px;
    font-family: "Arimo", Arial, sans-serif;
    font-size: 16px;
  }
  .isbn-note {
    position: absolute;
    left: 0; top: 80px;
    width: 180px;
    text-align: center;
    font-family: "Arimo", Arial, sans-serif;
    font-weight: 700;
    font-size: 15px;
    color: var(--muted);
  }

  /* Spine */
  .spine {
    position: absolute;
    left: 556px; top: 0;
    width: 88px; height: 825px;
    border-left: 2px solid var(--paper);
    border-right: 2px solid var(--paper);
  }
  .spine-author {
    position: absolute;
    left: 0; top: 22px;
    width: 84px;
    text-align: center;
    font-family: "Tinos", "Times New Roman", serif;
    font-weight: 700;
    font-size: 11px;
    line-height: 18px;
  }
  .spine-rule {
    position: absolute;
    left: 0; top: 84px;
    width: 84px; height: 6px;
    background: var(--paper);
  }
  .spine-title {
    position: absolute;
    left: 42px; top: 178px;
    transform-origin: 0 0;
    transform: rotate(90deg) translateY(-50%);
    font-family: "Bodoni Moda", "Didot", serif;
    font-weight: 900;
    font-size: 38px;
    line-height: 44px;
    color: var(--paper);
    white-space: nowrap;
    letter-spacing: 3px;
  }

  /* Front panel */
  .front {
    position: absolute;
    left: 644px; top: 0;
    width: 556px; height: 825px;
  }
  .title {
    position: absolute;
    left: 27px; top: 30px;
    font-family: "Bodoni Moda", "Didot", serif;
    font-weight: 900;
    font-size: 74px;
    line-height: 90px;
    color: var(--paper);
    letter-spacing: 1px;
  }
  .title-line { display: block; white-space: nowrap; }
  .title-globe {
    display: inline-block;
    width: 62px; height: 62px;
    vertical-align: -4px;
    margin-right: 2px;
  }
  .subtitle {
    position: absolute;
    left: 0; top: 397px;
    width: 536px;
    text-align: center;
    font-size: 32px;
    line-height: 40px;
  }
  .author {
    position: absolute;
    left: 0; top: 706px;
    width: 556px;
    text-align: center;
    font-family: "Stardos Stencil", "Impact", sans-serif;
    font-weight: 700;
    font-size: 50px;
    line-height: 64px;
    letter-spacing: 1px;
  }
</style>
</head>
<body>
<main class="cover">

  <section class="back">
    <h2 class="back-question">Do you have any idea how<br>we got to here?</h2>

    <p class="blurb blurb-1">Well, if you’re like 97.4% of the people walking the planet, you haven’t<br>got a clue. Sure, you might know a bit about a couple rivers in<br>Mesopotamia, how Socrates wandered around Athens asking questions<br>or how Martin Luther got ticked off one day and nailed a really long<br>essay to the door of a church. But to be honest (and don’t be embarrassed),<br>you’ve got some gaps.</p>

    <p class="blurb blurb-2">Be dense no more. In <em>Lanterns on the Tide</em>, Daniel Ashcombe takes you<br>through all the major tales, traditions and turning points of world history –<br>not just European history, but WORLD history. You’ll figure out real quick<br>that the West might have had some crowning moments, but for the whole<br>of human history, it’s been the Persians, the Indians, the Chinese, the<br>Muslims or some horse peoples from the steppe that have truly turned us<br>into the clever little creatures we are today.</p>

    <p class="blurb blurb-3">And when most world history books fade off once the Cold War comes to<br>a close, this sometimes cheekily-written tome just gets going. It finished<br>with a distinctively comprehensive look at the 21st century challenges facing<br>the nine major regions of today’s world – Africa, Latin America, Japan,<br>China, the Middle East, India, Russia, Europe and the United States.</p>

    <blockquote class="endorsement">“Daniel Ashcombe expertly understands exactly what his audience<br>wants to know, what they need to know. A page-turning account of<br>our proudest achievements and our most colossal bumblings. It’s world<br>history for the rest of us.” <cite>– Rafiq al-Nazari</cite></blockquote>

    <div class="isbn-block">
      <div class="publisher-band">Quillmark Publishing.Inc</div>
      <div class="isbn-number">ISBN 000-00-0000-0</div>
      <div class="isbn-note">SAMPLE ONLY</div>
    </div>
  </section>

  <section class="spine">
    <div class="spine-author">DANIEL<br>ASHCOMBE</div>
    <div class="spine-rule"></div>
    <div class="spine-title">LANTERNS ON THE TIDE</div>
  </section>

  <section class="front">
    <h1 class="title">
      <span class="title-line">LANTERNS</span>
      <span class="title-line"><svg class="title-globe" viewBox="0 0 62 62" role="img" aria-label="Small globe illustration forming the letter O"><circle cx="31" cy="31" r="28" fill="#e00000" stroke="#000" stroke-width="3"/></svg>N THE</span>
      <span class="title-line">TIDE</span>
    </h1>

    <p class="subtitle">The tales, traditions and<br>turning points of world history<br>and the regional challenges of today</p>

    <p class="author">DANIEL ASHCOMBE</p>
  </section>

</main>
</body>
</html>
```